Classy, Elegant, Simple Business Card Design

Looking to have a classy, simple, and elegant design. Want a top notch designed business card. I really like the look of the new veltro credit card. I also like the design I attached. I am trying to reach 21-29 year old females for booking us for there wedding or event. We offer Disc Jockey Service, Photo Booth Rentals, and Uplighting .

Target Market(s)

21-28 year old females

Contact Information for Business Card

Has to have logo, website, email, and phone number

Font styles to use
Other font styles liked:
• open to font choice, modern, clean
Designer to choose
33a6d7
0791cd
0555a3
ffffff

Requirements
Must have
• Has to have logo, website, email, and phone number
Nice to have
• I really like the design of the new veltro credit card. I also included my logo and some designs I like
Should not have
• clutter or too much info

```html
<!DOCTYPE html>
<html lang="en">
<head>
<meta charset="utf-8">
<title>Tidelight Event Group – Business Cards</title>
<link href="https://fonts.googleapis.com/css2?family=Lato:wght@300;400;700&display=swap" rel="stylesheet">
<style>
  :root {
    --bg: #d9d9d9;
    --card: #ffffff;
    --card-shade: #ececec;
    --sky: #33a6d7;
    --blue: #0791cd;
    --deep: #0555a3;
    --navy: #1c3a5e;
    --ink: #2b2b2b;
    --grey: #9a9a9a;
  }
  * { margin: 0; padding: 0; box-sizing: border-box; }
  html, body { width: 1200px; height: 900px; overflow: hidden; }
  body {
    background: var(--bg);
    font-family: 'Lato', sans-serif;
    position: relative;
  }
  .card {
    position: absolute;
    width: 580px;
    height: 330px;
    border-radius: 26px;
    background: radial-gradient(ellipse at 55% 40%, var(--card) 30%, var(--card-shade) 100%);
    box-shadow: 0 14px 30px rgba(0,0,0,.18);
  }
  .card-back { left: 90px; top: 90px; display: flex; align-items: center; justify-content: center; }
  .card-front { left: 530px; top: 480px; }

  .back-name {
    font-weight: 700;
    font-size: 46px;
    letter-spacing: 6px;
    color: var(--grey);
  }

  .brand { position: absolute; left: 42px; top: 58px; display: flex; align-items: center; gap: 12px; }
  .brand-dot { width: 18px; height: 18px; border-radius: 50%; background: var(--blue); }
  .brand-name { font-weight: 400; font-size: 30px; letter-spacing: 1px; color: var(--blue); line-height: 1.15; }

  .services {
    position: absolute; right: 34px; top: 48px;
    list-style: none; text-align: right;
    font-size: 19px; color: var(--ink); line-height: 1.35;
  }
  .services li { display: flex; align-items: center; justify-content: flex-end; gap: 8px; }
  .services li::after {
    content: ""; width: 9px; height: 9px; border-radius: 50%; background: var(--blue);
  }

  .contacts {
    position: absolute; left: 42px; bottom: 34px;
    list-style: none; font-size: 21px; color: var(--ink); line-height: 1.4;
  }
  .contacts li { display: flex; align-items: center; gap: 8px; }
  .contacts svg { width: 22px; height: 22px; flex: none; }
</style>
</head>
<body>

<section class="card card-back" aria-label="Card back">
  <span class="back-name">TIDELIGHT</span>
</section>

<section class="card card-front" aria-label="Card front">
  <div class="brand">
    <span class="brand-dot"></span>
    <span class="brand-name">Tidelight<br>Event Group</span>
  </div>

  <ul class="services">
    <li>Disc Jockey Service</li>
    <li>Photo Booth Rentals</li>
    <li>Uplighting</li>
  </ul>

  <ul class="contacts">
    <li>
      <svg viewBox="0 0 22 22" aria-hidden="true"><circle cx="11" cy="11" r="11" fill="var(--navy)"/><path d="M7 6.5c.6-.6 1.4-.5 1.8.1l1 1.5c.3.5.2 1-.2 1.4l-.6.5c.5 1.1 1.5 2.1 2.6 2.6l.5-.6c.4-.4.9-.5 1.4-.2l1.5 1c.6.4.7 1.2.1 1.8-2.5 2.3-9.2-4.3-8.1-8.1z" fill="#fff"/></svg>
      044-555 018 274
    </li>
    <li>
      <svg viewBox="0 0 22 22" aria-hidden="true"><circle cx="11" cy="11" r="11" fill="var(--navy)"/><rect x="5.5" y="7" width="11" height="8" fill="#fff"/><path d="M5.5 7l5.5 4.5L16.5 7" fill="none" stroke="var(--navy)" stroke-width="1.2"/></svg>
      info@tidelightevents.com
    </li>
    <li>
      <svg viewBox="0 0 22 22" aria-hidden="true"><circle cx="11" cy="11" r="11" fill="var(--navy)"/><circle cx="11" cy="11" r="5.5" fill="none" stroke="#fff" stroke-width="1.3"/><ellipse cx="11" cy="11" rx="2.4" ry="5.5" fill="none" stroke="#fff" stroke-width="1.1"/><line x1="5.5" y1="11" x2="16.5" y2="11" stroke="#fff" stroke-width="1.1"/></svg>
      www.tidelightevents.com
    </li>
  </ul>
</section>

</body>
</html>
```